I'm looking for a book cover with the Main title:
Quiet Mornings Along the Misty Coastal Lighthouse Trail

Subtitle: The Wanderer's Journal of Seaside Rambles

Looking for a clean design that attracts people to the book.

Open to all styles of design (plain text, animated characters, scenery) as long as the text is in basic font and easy to read.

This is to be put somewhere under the titles
Written By: Veselin Markhov

The back of the book will have:

"A physical, mental, emotional, and spiritual guide to fat loss. Going beyond calorie deficit diets and working out for hours a day in order to achieve results. It will help you get to the root cause of weight gain and give you the tools you need to take charge of your health and your life.

You will learn:
- The Best Foods to Eat for Fat Loss
- The Foods You Need to Avoid
- How to Heal Your Hormones
- Strategies to Overcome Emotional Eating
- Mindset and Motivation Tactics
- How to Meditate Without Losing Your Mind

I created this book to help those struggling with losing fat in a healthy, holistic, and sustainable way. It’s my sincere hope that this book gives you what you need in order to achieve your goals. "

Please place the photo somewhere on the back as well if it fits with the design.

Thank you for your time!

```html
<!DOCTYPE html>
<html lang="en">
<head>
<meta charset="utf-8">
<title>Quiet Mornings Along the Misty Coastal Lighthouse Trail — Cover</title>
<link href="https://fonts.googleapis.com/css2?family=Hind:wght@600;700&family=Noto+Serif:ital,wght@0,400;0,700;1,400&family=Oswald:wght@500&family=Source+Sans+3:wght@400&display=swap" rel="stylesheet">
<style>
  :root {
    --paper: #ffffff;
    --ink: #111111;
    --frame: #8a8a8a;
    --peach: #f6b793;
    --rose: #eb8d92;
    --pink: #df638e;
    --photo-green: #6f8a4f;
    --photo-skin: #b98866;
  }
  * { margin: 0; padding: 0; box-sizing: border-box; }
  html, body { width: 1200px; height: 829px; overflow: hidden; background: var(--paper); }
  .spread { position: relative; width: 1200px; height: 829px; }
  .cover-panel {
    position: absolute; top: 15px; width: 567px; height: 805px;
    border: 1px solid var(--frame); background: var(--paper); overflow: hidden;
  }
  .back-cover { left: 13px; }
  .front-cover { left: 619px; }

  .back-art {
    position: absolute; left: 427px; top: 45px; width: 82px; height: 733px;
    border-radius: 41px;
    background: linear-gradient(180deg, var(--rose) 0%, var(--peach) 38%, var(--pink) 80%, var(--rose) 100%);
    opacity: 0.85;
  }
  .front-art {
    position: absolute; left: 96px; top: 162px; width: 400px; height: 470px;
    border-radius: 48px;
    background: radial-gradient(ellipse at 50% 50%, rgba(246,183,147,0.12) 0%, rgba(235,141,146,0.22) 65%, rgba(223,99,142,0.28) 100%);
  }

  .back-content { position: absolute; left: 41px; top: 57px; width: 380px; color: var(--ink); }
  .blurb { font-family: "Source Sans 3", sans-serif; font-size: 16px; line-height: 27px; white-space: nowrap; }
  .learn-heading {
    font-family: "Hind", sans-serif; font-weight: 700; font-size: 18.5px;
    margin-top: 26px; line-height: 24px;
  }
  .learn-list { list-style: none; font-family: "Hind", sans-serif; font-weight: 700; font-size: 18.5px; }
  .learn-list li { position: relative; padding-left: 23px; line-height: 22px; margin-top: 10.5px; }
  .learn-list li::before {
    content: ""; position: absolute; left: 3px; top: 7px;
    width: 8px; height: 8px; border-radius: 50%; background: var(--ink);
  }

  .author-heading {
    position: absolute; left: 41px; top: 548px;
    font-family: "Noto Serif", serif; font-weight: 700; font-size: 18px; color: var(--ink);
  }
  .author-photo {
    position: absolute; left: 43px; top: 591px; width: 111px; height: 111px; border-radius: 50%;
    background: radial-gradient(circle at 50% 45%, var(--photo-skin) 0%, #7d6048 45%, var(--photo-green) 80%);
  }
  .author-note {
    position: absolute; left: 41px; top: 584px;
    font-family: "Noto Serif", serif; font-style: italic; font-size: 15.5px; line-height: 22.7px; color: var(--ink);
  }
  .author-note span { display: block; white-space: nowrap; }

  .front-text { position: absolute; inset: 0; width: 100%; height: 100%; }
</style>
</head>
<body>
<main class="spread">

  <section class="cover-panel back-cover" aria-label="Back cover">
    <div class="back-art" role="img" aria-label="Curved pink waist-silhouette illustration with splash marks"></div>

    <div class="back-content">
      <p class="blurb">A physical, mental, emotional, and spiritual guide to<br>fat loss. Going beyond calorie deficit diets and working<br>out for hours a day in order to achieve results. It will<br>help you get to the root cause of weight gain and give<br>you the tools you need to take charge of your health<br>and your life.</p>
      <h2 class="learn-heading">You will learn:</h2>
      <ul class="learn-list">
        <li>The Best Foods to Eat for Fat Loss</li>
        <li>The Foods You Need to Avoid</li>
        <li>How to Heal Your Hormones</li>
        <li>Strategies to Overcome Emotional Eating</li>
        <li>Mindset and Motivation Tactics</li>
        <li>How to Meditate Without Losing<br>Your Mind</li>
      </ul>
    </div>

    <h2 class="author-heading">About the Author</h2>
    <div class="author-photo" role="img" aria-label="Portrait photo of the author, Veselin Markhov"></div>
    <p class="author-note">
      <span style="margin-left:111px">I created this book to help</span>
      <span style="margin-left:123px">those struggling with losing</span>
      <span style="margin-left:124px">fat in a healthy, holistic, and</span>
      <span style="margin-left:124px">sustainable way. It’s my</span>
      <span style="margin-left:114px">sincere hope that this book</span>
      <span style="margin-left:89px">gives you what you need in order</span>
      <span>to achieve your goals.</span>
    </p>
  </section>

  <section class="cover-panel front-cover" aria-label="Front cover">
    <div class="front-art" role="img" aria-label="Pink waist-silhouette illustration with splash marks framing the title"></div>
    <svg class="front-text" viewBox="0 0 1087 1542" preserveAspectRatio="none">
      <defs>
        <linearGradient id="title-fill" x1="0" y1="0" x2="0.3" y2="1">
          <stop offset="0" stop-color="var(--peach)"/>
          <stop offset="0.6" stop-color="var(--rose)"/>
          <stop offset="1" stop-color="var(--pink)"/>
        </linearGradient>
      </defs>
      <text x="545" y="125" text-anchor="middle" font-family="'Noto Serif', serif" font-size="44" fill="var(--ink)">The Wanderer's Journal of Seaside Rambles</text>

      <g class="main-title" fill="url(#title-fill)" font-family="'Oswald', sans-serif" font-weight="500" text-anchor="middle">
        <title>Quiet Mornings Along the Misty Coastal Lighthouse Trail</title>
        <text x="545" y="358" font-size="95" textLength="240" lengthAdjust="spacingAndGlyphs">QUIET</text>
        <text x="545" y="580" font-size="215" textLength="360" lengthAdjust="spacingAndGlyphs">MORNINGS</text>
        <text x="545" y="712" font-size="125" textLength="330" lengthAdjust="spacingAndGlyphs">ALONG THE</text>
        <text x="545" y="810" font-size="95" textLength="360" lengthAdjust="spacingAndGlyphs">MISTY</text>
        <text x="545" y="955" font-size="150" textLength="470" lengthAdjust="spacingAndGlyphs">COASTAL</text>
        <text x="545" y="1100" font-size="140" textLength="570" lengthAdjust="spacingAndGlyphs">LIGHTHOUSE</text>
        <text x="545" y="1228" font-size="130" textLength="400" lengthAdjust="spacingAndGlyphs">TRAIL</text>
      </g>

      <text x="545" y="1455" text-anchor="middle" font-family="'Noto Serif', serif" font-size="105" fill="var(--ink)" textLength="740" lengthAdjust="spacingAndGlyphs">Veselin Markhov</text>
    </svg>
  </section>

</main>
</body>
</html>
```